Business Card Design

We are looking for a double sided business card.

On one side would be our logo

On the Other Side

Daniel Workby
Sales and Marketing

Phone/Text Logo and 530-471-6328
Email Logo and info@gildedcritters.example
Website Logo and www.gildedcritters.example
Facebook Logo and gilded critters
Instagram Logo and gilded_critters

Target Market(s)

Pet owners

Contact Information for Business Card

In project description

Requirements
Must have
• Logo

```html
<!DOCTYPE html>
<html lang="en">
<head>
<meta charset="utf-8">
<title>Gilded Critters – Business Card</title>
<link href="https://fonts.googleapis.com/css2?family=Arimo:wght@400;700&display=swap" rel="stylesheet">
<style>
  :root {
    --backdrop: #2b2b2d;
    --card: #050505;
    --orange: #f08a24;
    --amber: #f6b21c;
    --silver: #d9d9d9;
    --white: #ffffff;
  }
  * { margin: 0; padding: 0; box-sizing: border-box; }
  html, body { width: 1200px; height: 874px; overflow: hidden; }
  body {
    background: var(--backdrop);
    font-family: "Arimo", Arial, sans-serif;
    position: relative;
  }
  .card {
    position: absolute;
    width: 620px;
    height: 354px;
    background: var(--card);
    border-radius: 18px;
    overflow: hidden;
    box-shadow: 0 10px 30px rgba(0,0,0,.45);
  }
  .card--front { left: 450px; top: 50px; }
  .card--back  { left: 130px; top: 470px; }

  /* front */
  .brand {
    position: absolute;
    display: flex;
    align-items: center;
    gap: 14px;
  }
  .brand__dot {
    border-radius: 50%;
    background: var(--orange);
    flex: none;
  }
  .brand__name {
    color: var(--silver);
    font-weight: 700;
    text-transform: uppercase;
    letter-spacing: 1px;
    white-space: nowrap;
  }
  .card--front .brand { left: 50%; top: 50%; transform: translate(-50%, -50%); }
  .card--front .brand__dot { width: 46px; height: 46px; }
  .card--front .brand__name { font-size: 46px; }

  .social {
    position: absolute;
    right: 28px;
    top: 120px;
    display: flex;
    gap: 10px;
  }
  .social__badge {
    width: 30px; height: 30px;
    border-radius: 50%;
    background: var(--orange);
  }

  /* back */
  .card--back .brand { left: 26px; top: 28px; }
  .card--back .brand__name { font-size: 30px; }

  .mark-area {
    position: absolute;
    left: 40px;
    top: 100px;
    width: 360px;
    height: 254px;
    border-radius: 160px 160px 0 0;
    background: linear-gradient(135deg, var(--orange) 0%, var(--amber) 45%, var(--silver) 100%);
    opacity: .9;
  }

  .person {
    position: absolute;
    right: 30px;
    top: 110px;
    text-align: right;
  }
  .person__name {
    color: var(--orange);
    font-weight: 700;
    font-size: 26px;
    text-transform: uppercase;
  }
  .person__title {
    color: var(--white);
    font-size: 16px;
    margin-top: 4px;
  }

  .contact {
    position: absolute;
    right: 24px;
    bottom: 48px;
    list-style: none;
    text-align: right;
  }
  .contact__item {
    display: flex;
    justify-content: flex-end;
    align-items: center;
    gap: 10px;
    color: var(--white);
    font-size: 16px;
    line-height: 24px;
  }
  .contact__icon { width: 14px; height: 14px; fill: var(--orange); flex: none; }
</style>
</head>
<body>

  <section class="card card--front" aria-label="Business card front">
    <div class="brand">
      <span class="brand__dot"></span>
      <span class="brand__name">Gilded Critters</span>
    </div>
    <div class="social" aria-label="Social profiles">
      <span class="social__badge"></span>
      <span class="social__badge"></span>
    </div>
  </section>

  <section class="card card--back" aria-label="Business card back">
    <div class="brand">
      <span class="brand__name">Gilded Critters</span>
    </div>

    <div class="mark-area" role="img" aria-label="Large brand symbol decoration in orange and silver"></div>

    <div class="person">
      <p class="person__name">Daniel Workby</p>
      <p class="person__title">Sales and Marketing</p>
    </div>

    <ul class="contact">
      <li class="contact__item">530-471-6328
        <svg class="contact__icon" viewBox="0 0 16 16" aria-hidden="true"><path d="M3.5 1.5l2.5 0 1 3.5-1.6 1.2c.8 1.8 2.2 3.2 4 4l1.2-1.6 3.5 1v2.5c0 .8-.7 1.4-1.5 1.4C6.9 13.5 2.5 9.1 2.1 3c0-.8.6-1.5 1.4-1.5z"/></svg>
      </li>
      <li class="contact__item">info@gildedcritters.example
        <svg class="contact__icon" viewBox="0 0 16 16" aria-hidden="true"><path d="M1 3h14v10H1z M1.5 3.5 8 9l6.5-5.5" stroke="#050505" stroke-width="1.2"/></svg>
      </li>
      <li class="contact__item">www.gildedcritters.example
        <svg class="contact__icon" viewBox="0 0 16 16" aria-hidden="true"><circle cx="8" cy="8" r="7"/><path d="M1 8h14M8 1c3 3.5 3 10.5 0 14M8 1c-3 3.5-3 10.5 0 14" stroke="#050505" stroke-width="1" fill="none"/></svg>
      </li>
    </ul>
  </section>

</body>
</html>
```